Business Card Design Project

This is a new division in our company. "Kestrel Wellsite & Safety" This is a Oilfield Safety company. I have included our new logo. I also have given our other business card. We love double sided with lots of color. We like to stand out. Please DO NOT duplicate our other card and bring your design into it. See all attached files.
Reason: forgot to change this when I posted it.
Here is the correct information card.
www.kestrelwellsitesafety.example
Dwayne@kestrelwellsitesafety.example
Reason: revision for a few.
Reason: was traveling and need to review designs.
Target Market(s)
Oil and Gas industry. Masculine look.
Industry/Entity Type
Business
Look and feel

```html
<!DOCTYPE html>
<html lang="en">
<head>
<meta charset="utf-8">
<title>Kestrel Wellsite &amp; Safety – Business Card</title>
<link rel="stylesheet" href="https://fonts.googleapis.com/css2?family=Michroma&family=Roboto+Condensed:wght@400&display=swap">
<style>
  :root {
    --stage: #939393;
    --card: #ffffff;
    --orange: #ee4b23;
    --green: #7bbd3c;
    --teal: #2fb3aa;
    --text: #4a4a4a;
    --yellow: #f6ec5a;
    --sky: #6fb8e6;
  }
  * { margin: 0; padding: 0; box-sizing: border-box; }
  html, body { width: 1200px; height: 1000px; overflow: hidden; }
  body { background: var(--stage); position: relative; font-family: "Roboto Condensed", sans-serif; }

  .card {
    position: absolute; width: 543px; height: 318px;
    background: var(--card); overflow: hidden;
    box-shadow: 3px 4px 4px rgba(0,0,0,.45);
  }
  .card--front { left: 118px; top: 92px; }
  .card--back  { left: 513px; top: 493px; }

  .swirl {
    position: absolute; inset: 0;
    background:
      radial-gradient(ellipse 38% 50% at 0% 45%, rgba(125,200,230,.35), rgba(255,255,255,0) 100%),
      radial-gradient(ellipse 125% 150% at 105% -10%,
        #fdc766 0%, var(--yellow) 16%, #a2d067 30%, #5fb27a 42%, #5fc0b4 54%, var(--sky) 66%, rgba(255,255,255,0) 80%);
  }

  .band { position: absolute; left: 0; bottom: 0; width: 100%; height: 18px; }

  .logo-word {
    position: absolute; color: var(--teal);
    font-family: "Michroma", sans-serif; font-weight: 400;
    display: flex; align-items: center;
  }
  .logo-word__mark { background: var(--orange); flex: none; }

  .card--front .logo-word {
    left: 56px; top: 110px; width: 140px; font-size: 15px; line-height: 1.35;
    flex-direction: column; align-items: flex-start; gap: 10px;
  }
  .card--front .logo-word__mark { width: 22px; height: 22px; }

  .card--back .logo-word {
    left: 78px; top: 118px; width: 400px; font-size: 25px; line-height: 1.3; gap: 16px;
  }
  .card--back .logo-word__mark { width: 30px; height: 30px; }

  .person { position: absolute; left: 253px; top: 42px; }
  .person__name {
    font-family: "Michroma", sans-serif; font-weight: 400;
    color: var(--orange); font-size: 17px; line-height: 1;
  }
  .person__role { color: var(--text); font-size: 14px; margin-top: 6px; margin-left: 2px; }

  .contacts { position: absolute; left: 253px; top: 170px; list-style: none; }
  .contacts li {
    display: flex; align-items: center; gap: 8px;
    color: var(--text); font-size: 14px; height: 17.6px; white-space: nowrap;
  }
  .contacts svg { width: 14px; height: 14px; flex: none; }
</style>
</head>
<body>

<section class="card card--front">
  <div class="swirl" role="img" aria-label="Soft swirling rainbow light rays in yellow, green, teal and blue"></div>

  <div class="logo-word">
    <span class="logo-word__mark"></span>
    <span>Kestrel Wellsite &amp; Safety</span>
  </div>

  <div class="person">
    <p class="person__name">Dwayne Harlow</p>
    <p class="person__role">Managing Director</p>
  </div>

  <ul class="contacts">
    <li><svg viewBox="0 0 14 14"><rect width="14" height="14" rx="2" fill="#ee4b23"/><rect x="4.5" y="2.5" width="5" height="9" rx="1" fill="#fff"/></svg>+1 508.555.0187</li>
    <li><svg viewBox="0 0 14 14"><rect width="14" height="14" rx="2" fill="#ee4b23"/><path d="M4 3l2 0 1 2.5-1.2 1a6 6 0 0 0 2.7 2.7l1-1.2L12 9v2c-5 0-8-3-8-8z" fill="#fff"/></svg>+1 508.555.0188</li>
    <li><svg viewBox="0 0 14 14"><rect width="14" height="14" rx="2" fill="#ee4b23"/><rect x="3" y="6" width="8" height="5" fill="#fff"/><rect x="4.5" y="3" width="5" height="3" fill="#fff"/></svg>+1 508.555.0189</li>
    <li><svg viewBox="0 0 14 14"><rect width="14" height="14" rx="2" fill="#ee4b23"/><rect x="3" y="4" width="8" height="6" fill="#fff"/><path d="M3 4l4 3.5L11 4" stroke="#ee4b23" fill="none"/></svg>Dwayne@kestrelwellsitesafety.example</li>
    <li><svg viewBox="0 0 14 14"><rect width="14" height="14" rx="2" fill="#ee4b23"/><circle cx="7" cy="7" r="4" fill="none" stroke="#fff"/><path d="M3 7h8M7 3v8" stroke="#fff"/></svg>www.kestrelwellsitesafety.example</li>
    <li><svg viewBox="0 0 14 14"><rect width="14" height="14" rx="2" fill="#ee4b23"/><path d="M7 12L4 7a3 3 0 1 1 6 0z" fill="#fff"/><circle cx="7" cy="6" r="1.2" fill="#ee4b23"/></svg>18 Harbour Lane, Redgum Flats, NT, 0872</li>
  </ul>

  <svg class="band" viewBox="0 0 543 18" preserveAspectRatio="none">
    <rect x="0" y="0" width="543" height="18" fill="#ee4b23"/>
    <path d="M0 1 H360 Q405 1 428 18 H0z" fill="#fff"/>
    <path d="M0 1 H352 Q392 1 412 18 H0z" fill="#7bbd3c"/>
  </svg>
</section>

<section class="card card--back">
  <div class="swirl" role="img" aria-label="Soft swirling rainbow light rays in yellow, green, teal and blue"></div>

  <div class="logo-word">
    <span class="logo-word__mark"></span>
    <span>Kestrel Wellsite &amp; Safety</span>
  </div>

  <svg class="band" viewBox="0 0 543 18" preserveAspectRatio="none">
    <rect x="0" y="0" width="543" height="18" fill="#ee4b23"/>
    <path d="M0 1 H360 Q405 1 428 18 H0z" fill="#fff"/>
    <path d="M0 1 H352 Q392 1 412 18 H0z" fill="#7bbd3c"/>
  </svg>
</section>

</body>
</html>
```